Lumo Academics - new College Consulting company in San Francisco needs a flyer design

We need a logo design for a new college admissions consulting business in San Francisco Bay Area and San Jose called 'Lumo Academics'. We plan to develop tailor-made strategies for each students dreams and aspirations and will help provide them with online classes and in-person consulting starting Summer 2022.
Lumo Academics plans on providing a free first time consulting to attract clients and grow our client base from there.
Lumo Academics has a small team of consultants who have degrees from Economics/Business, Biology, and Computer Science who can provide tailored guidance to meet student and parent expectations and spend the time to walk them throughout the process.
Please refer to attached logos for the company and to create a flyer.
Competitive College Consulting
Education Consulting

```html
<!DOCTYPE html>
<html lang="en">
<head>
<meta charset="utf-8">
<title>Lumo Academics – Flyer</title>
<link rel="stylesheet" href="https://fonts.googleapis.com/css2?family=Poppins:wght@300;400;500;600;700;800&family=Anton&family=Crimson+Text&display=swap">
<style>
  :root{
    --coral:#f58a84;
    --coral-deep:#e9605b;
    --coral-soft:#fbb3ad;
    --badge:#d9505a;
    --ink:#232323;
    --panel:#2a2a2a;
    --white:#ffffff;
    --paper:#f3f3f3;
    --gold:#f2b41c;
    --stage:#ececec;
  }
  *{margin:0;padding:0;box-sizing:border-box}
  html,body{width:1200px;height:1200px;overflow:hidden}
  body{background:var(--stage);font-family:"Poppins",sans-serif;color:var(--ink)}
  .flyer{position:absolute;left:200px;top:34px;width:800px;height:1132px;background:var(--white);overflow:hidden}
  .abs{position:absolute}

  /* header */
  .brand{left:52px;top:62px;text-align:right;width:240px}
  .brand-name{font-family:"Poppins",sans-serif;font-weight:500;font-size:21px;color:var(--ink);line-height:1.1}
  .brand-tagline{font-family:"Crimson Text",serif;font-size:17px;color:var(--ink);line-height:1.2}
  .brand-mark{left:302px;top:72px;width:38px;height:38px;border-radius:50%;background:var(--ink)}

  /* hero */
  .hero{left:0;top:125px;width:800px;height:305px;background:linear-gradient(90deg,var(--coral) 0%,var(--coral-soft) 55%,var(--coral) 100%)}
  .hero-scene{left:330px;top:125px;width:470px;height:420px;background:linear-gradient(180deg,rgba(255,255,255,.18),rgba(233,96,91,.35))}
  .headline{left:50px;top:166px;font-weight:800;font-size:61px;line-height:.98;letter-spacing:-1px}
  .headline .dark{color:var(--ink);display:block}
  .headline .light{color:var(--white);display:block}
  .intro{left:52px;top:318px;border-left:5px solid var(--white);padding-left:12px;width:380px;font-weight:500;font-size:19.5px;line-height:1.33;color:var(--ink)}

  /* team panel */
  .panel-shape{left:0;top:429px}
  .team-title{left:48px;top:458px;color:var(--white);font-weight:300;font-size:22px}
  .team-title strong{color:var(--coral);font-weight:600}
  .team-text{left:48px;top:488px;width:360px;color:var(--white);font-weight:300;font-size:14.5px;line-height:1.35}
  .gold-rule{left:48px;top:532px;width:49px;height:3px;background:var(--gold)}
  .degrees{left:48px;top:556px;list-style:none}
  .degrees li{display:flex;align-items:center;height:39px;color:var(--white);font-weight:600;font-size:19.5px}
  .degrees svg{width:32px;height:28px;margin-right:10px}

  /* student photo */
  .student-photo{left:430px;top:40px;width:370px;height:660px;background:linear-gradient(180deg,#b98b72 0%,#e25a55 45%,#c94a4a 70%,#9a9a9a 100%);border-radius:160px 160px 0 0}

  /* free badge */
  .badge{left:515px;top:537px}
  .badge-word{left:533px;top:566px;width:190px;text-align:center;font-family:"Anton",sans-serif;font-size:86px;line-height:1;color:var(--white);letter-spacing:1px}
  .badge-sub{left:533px;top:665px;width:190px;text-align:center;font-family:"Anton",sans-serif;font-size:16px;color:var(--white);letter-spacing:.2px}

  /* why section */
  .lower{left:0;top:700px;width:800px;height:432px;background:linear-gradient(180deg,#f7f7f7,#e9e9e9)}
  .lower-scene{left:0;top:755px;width:800px;height:377px;background:linear-gradient(90deg,rgba(200,200,200,.35),rgba(230,230,230,.1) 60%,rgba(210,210,210,.3))}
  .top-rule{left:0;top:698px;width:800px;height:2px;background:var(--coral-deep)}
  .why-band{left:0;top:700px}
  .why-title{left:49px;top:711px;font-weight:700;font-size:26px;color:var(--ink)}
  .why-title span{color:var(--white)}
  .reason{width:300px;font-weight:500;font-size:12.3px;line-height:1.25;color:var(--ink);display:flex;gap:10px}
  .reason svg{flex:none;width:30px;height:28px}
  .r1{left:40px;top:784px}
  .r2{left:40px;top:832px}
  .r3{left:422px;top:784px;width:340px}
  .r4{left:422px;top:832px;width:340px}
  .divider{left:396px;top:776px;height:106px;border-left:1.5px dotted #777}

  .grads-photo{left:0;top:889px;width:386px;height:243px;background:linear-gradient(180deg,#eae4e2 0%,#d8413f 45%,#151515 80%);border-radius:120px 120px 0 0}

  .service{display:flex;gap:10px;align-items:flex-start}
  .service-icon{width:70px;height:70px;border-radius:12px;background:var(--ink);border:3px solid var(--white);box-shadow:-4px -4px 0 var(--coral-deep);display:flex;align-items:center;justify-content:center}
  .service-label{font-weight:500;font-size:18px;line-height:1.15;color:var(--ink)}
  .s1{left:410px;top:918px}
  .s2{left:615px;top:918px}

  .contact-rule{left:430px;top:1020px;width:346px;height:1px;background:#bbb}
  .phone-line{left:429px;top:1028px;display:flex;align-items:center;gap:8px}
  .phone-line .lead{font-weight:500;font-size:21px}
  .phone-line .num{font-weight:600;font-size:32px;letter-spacing:-.3px}
  .detail{left:430px;font-weight:500;font-size:12.5px;display:flex;align-items:center;gap:6px}
  .address{top:1066px}
  .email{top:1085px}
</style>
</head>
<body>
<main class="flyer">

  <header>
    <div class="abs brand">
      <div class="brand-name">Lumo Academics</div>
      <div class="brand-tagline">Learning is a phenomenom</div>
    </div>
    <div class="abs brand-mark"></div>
  </header>

  <section class="hero-block">
    <div class="abs hero"></div>
    <div class="abs hero-scene" role="img" aria-label="Campus walkway with students, tinted coral"></div>
    <h1 class="abs headline"><span class="dark">LUMO</span><span class="light">ACADEMICS</span></h1>
    <p class="abs intro">We plan to develop tailor-made strategies for each students dreams and aspirations</p>
  </section>

  <svg class="abs panel-shape" width="800" height="272" viewBox="0 0 800 272">
    <path d="M0 0 H360 C385 0 390 10 400 30 C410 50 420 55 445 55 H800 V272 H0 Z" fill="var(--panel)"/>
  </svg>

  <div class="abs student-photo" role="img" aria-label="Smiling student in glasses and a red shirt holding a stack of books"></div>

  <section class="team">
    <h2 class="abs team-title">The character of <strong>Success</strong></h2>
    <p class="abs team-text">Lumo Academics has a small team of consultants who have degrees from</p>
    <div class="abs gold-rule"></div>
    <ul class="abs degrees">
      <li><svg viewBox="0 0 32 28"><path d="M16 3 L31 10 L16 17 L1 10 Z" fill="var(--coral)"/><path d="M8 14 V21 C12 24 20 24 24 21 V14 L16 18 Z" fill="var(--coral)"/><path d="M4 11 V22" stroke="var(--coral)" stroke-width="2"/></svg>ECONOMICS/BUSINESS</li>
      <li><svg viewBox="0 0 32 28"><path d="M16 3 L31 10 L16 17 L1 10 Z" fill="var(--coral)"/><path d="M8 14 V21 C12 24 20 24 24 21 V14 L16 18 Z" fill="var(--coral)"/><path d="M4 11 V22" stroke="var(--coral)" stroke-width="2"/></svg>BIOLOGY</li>
      <li><svg viewBox="0 0 32 28"><path d="M16 3 L31 10 L16 17 L1 10 Z" fill="var(--coral)"/><path d="M8 14 V21 C12 24 20 24 24 21 V14 L16 18 Z" fill="var(--coral)"/><path d="M4 11 V22" stroke="var(--coral)" stroke-width="2"/></svg>COMPUTER SCIENCE</li>
    </ul>
  </section>

  <section class="why">
    <div class="abs lower"></div>
    <div class="abs lower-scene" role="img" aria-label="Faded greyscale campus buildings"></div>
    <div class="abs top-rule"></div>
    <svg class="abs why-band" width="340" height="56" viewBox="0 0 340 56">
      <path d="M0 0 H340 C325 8 318 30 310 44 C305 52 298 56 285 56 H0 Z" fill="var(--coral)"/>
    </svg>
    <h2 class="abs why-title">WHY CHOOSE <span>US</span></h2>

    <div class="abs reason r1"><svg viewBox="0 0 32 28"><path d="M16 3 L31 10 L16 17 L1 10 Z" fill="var(--coral)"/><path d="M8 14 V21 C12 24 20 24 24 21 V14 L16 18 Z" fill="var(--coral)"/></svg><p>We plan to develop tailor-made strategies for each students dreams and aspirations</p></div>
    <div class="abs reason r2"><svg viewBox="0 0 30 28"><path d="M2 5 C7 3 12 4 15 7 C18 4 23 3 28 5 V24 C23 22 18 23 15 25 C12 23 7 22 2 24 Z" fill="none" stroke="var(--coral)" stroke-width="2.5"/><path d="M15 7 V25" stroke="var(--coral)" stroke-width="2"/></svg><p>Lumo Academics plans on providing a free first time consulting to attract clients and grow our client base from there</p></div>
    <div class="abs divider"></div>
    <div class="abs reason r3"><svg viewBox="0 0 30 28"><rect x="13" y="2" width="15" height="12" fill="none" stroke="var(--coral-deep)" stroke-width="2"/><circle cx="7" cy="7" r="4" fill="var(--coral-deep)"/><path d="M2 26 V14 H12 V26 Z" fill="var(--coral-deep)"/></svg><p>We will help provide them with online classes and in-person consulting starting Summer 2022</p></div>
    <div class="abs reason r4"><svg viewBox="0 0 30 28"><circle cx="15" cy="4" r="3" fill="var(--coral-deep)"/><path d="M15 8 V26 M4 15 H26 M4 15 L8 11 M4 15 L8 19 M26 15 L22 11 M26 15 L22 19" stroke="var(--coral-deep)" stroke-width="2.5" fill="none"/></svg><p>We provide tailored guidance to meet student and parent expectations and spend the time to walk them throughout the process</p></div>

    <div class="abs grads-photo" role="img" aria-label="Three graduates in caps and gowns holding diplomas"></div>

    <div class="abs service s1">
      <div class="service-icon"><svg width="38" height="34" viewBox="0 0 38 34"><rect x="4" y="2" width="30" height="18" rx="2" fill="none" stroke="#fff" stroke-width="2"/><path d="M18 7 L25 11 L18 15 Z" fill="#fff"/><circle cx="9" cy="26" r="3" fill="#fff"/><circle cx="19" cy="26" r="3" fill="#fff"/><circle cx="29" cy="26" r="3" fill="#fff"/><path d="M4 34 C4 30 14 30 14 34 M14 34 C14 30 24 30 24 34 M24 34 C24 30 34 30 34 34" fill="#fff"/></svg></div>
      <p class="service-label">Online<br>classes<br>Available</p>
    </div>
    <div class="abs service s2">
      <div class="service-icon"><svg width="38" height="34" viewBox="0 0 38 34"><rect x="14" y="1" width="12" height="8" rx="2" fill="#fff"/><circle cx="10" cy="14" r="3" fill="#fff"/><circle cx="28" cy="14" r="3" fill="#fff"/><path d="M4 24 C4 18 16 18 16 24 Z M22 24 C22 18 34 18 34 24 Z" fill="#fff"/><rect x="2" y="25" width="34" height="3" fill="#fff"/><path d="M6 28 V34 M32 28 V34" stroke="#fff" stroke-width="2"/></svg></div>
      <p class="service-label">In person<br>Consulting</p>
    </div>

    <div class="abs contact-rule"></div>
    <div class="abs phone-line">
      <span class="lead">Text us</span>
      <svg width="30" height="26" viewBox="0 0 30 26"><path d="M2 2 H20 V14 H9 L4 18 V14 H2 Z" fill="var(--coral)"/><path d="M12 9 H28 V21 H26 V25 L21 21 H12 Z" fill="var(--coral-deep)"/></svg>
      <span class="num">415 555 0148</span>
    </div>
    <p class="abs detail address"><svg width="10" height="14" viewBox="0 0 10 14"><path d="M5 0 C2 0 0 2 0 5 C0 8 5 14 5 14 C5 14 10 8 10 5 C10 2 8 0 5 0 Z" fill="var(--coral-deep)"/><circle cx="5" cy="5" r="2" fill="#fff"/></svg>Harbor View Ave. Suite 210, Fremont, CA 94538</p>
    <p class="abs detail email"><svg width="12" height="9" viewBox="0 0 12 9"><rect width="12" height="9" fill="var(--coral-deep)"/><path d="M0 0 L6 5 L12 0" stroke="#fff" fill="none"/></svg>hello@lumoacademics.com</p>
  </section>

  <svg class="abs badge" width="230" height="224" viewBox="0 0 230 224">
    <path d="M30 6 H200 C216 6 226 16 226 32 V150 C226 166 216 176 200 176 H142 L112 218 L92 176 H30 C14 176 4 166 4 150 V32 C4 16 14 6 30 6 Z" fill="#b23c46"/>
    <path d="M26 2 H196 C212 2 222 12 222 28 V146 C222 162 212 172 196 172 H138 L110 212 L88 172 H26 C10 172 0 162 0 146 V28 C0 12 10 2 26 2 Z" fill="var(--badge)"/>
  </svg>
  <div class="abs badge-word">FREE</div>
  <div class="abs badge-sub">FIRST TIME CONSULTING</div>

</main>
</body>
</html>
```